Business card for Drone Aerial

I need a business card designed keeping in mind I want to do post cards also with a similar design.
Both sides of the card would be cool.
I have a skylark 5 max and would like a picture of it on the front of the card. Similar to one I attached.
I really like the look of a drone in the air and the background pic a little blurry. I attached a few images as IDEAS.
Some special things I want to be on the card additional to the normal business card info:
"Aerial Photography" or "Low Altitude Aerial Photography"?
"ZQB# 90817263"

I like modern and creative. My Favorite color is blue and I like blue on white.
I do not have a business name and am not going to have one. When they read "Aerial Photography" and see the drone and image they will know what the card is for.

FYI, The attached pictures are just images from framewillow and just samples/ideas.

Target Market(s)

Real estate, construction, events

Industry/Entity Type

Business

Contact Information for Business Card

Also Definitely want to contain, my name, my number and email address.

Requirements
Must have
• "ZQB# 90817263"
• "Aerial Photography"

```html
<!DOCTYPE html>
<html lang="en">
<head>
<meta charset="utf-8">
<title>Aerial Photography – Business Card</title>
<link rel="stylesheet" href="https://fonts.googleapis.com/css2?family=Open+Sans:wght@400;600;700&display=swap">
<style>
  :root {
    --backdrop: #d9d9d9;
    --card-blue: #2796e0;
    --card-blue-light: #5cb6f0;
    --white: #ffffff;
    --tag-black: #1b1b1b;
    --sky-teal: #8fc4b8;
    --sky-mist: #b9d3c3;
    --dusk-amber: #c9772c;
    --city-dark: #2a1d12;
    --drone-white: #f1ece4;
  }
  * { box-sizing: border-box; margin: 0; padding: 0; }
  html, body {
    width: 1200px; height: 960px; overflow: hidden;
    background: var(--backdrop);
    font-family: "Open Sans", Arial, sans-serif;
  }
  .sheet {
    width: 1200px; height: 960px;
    display: flex; flex-direction: column; align-items: center; justify-content: center;
    gap: 32px;
  }
  .card {
    position: relative;
    width: 760px; height: 434px;
    overflow: hidden;
    box-shadow: 0 6px 18px rgba(0,0,0,.25);
  }

  /* Front side */
  .card-front .scene-photo {
    position: absolute; inset: 0;
    background:
      radial-gradient(ellipse 40% 30% at 55% 62%, rgba(240,150,50,.75), transparent 70%),
      radial-gradient(ellipse 60% 35% at 30% 85%, rgba(224,138,42,.55), transparent 75%),
      linear-gradient(180deg, var(--sky-mist) 0%, var(--sky-teal) 22%, #6f8f78 40%, var(--dusk-amber) 58%, #5a3a1c 75%, var(--city-dark) 100%);
  }
  .card-front .drone-photo {
    position: absolute; left: 430px; top: 150px;
    width: 260px; height: 230px;
    border-radius: 40%;
    background: radial-gradient(ellipse at 50% 45%, rgba(241,236,228,.85) 0%, rgba(241,236,228,.45) 45%, transparent 72%);
  }
  .license-tag {
    position: absolute; top: 56px; left: 46px; z-index: 2;
    background: var(--tag-black); color: var(--white);
    font-size: 22px; font-weight: 600; letter-spacing: .5px;
    padding: 8px 22px;
  }
  .headline {
    position: absolute; left: 40px; top: 124px; z-index: 2;
    font-weight: 600; line-height: .98;
    color: transparent;
    -webkit-text-stroke: 2px var(--white);
    letter-spacing: .5px;
  }
  .headline .line-one { display: block; font-size: 96px; padding-left: 50px; }
  .headline .line-two { display: block; font-size: 96px; }

  /* Back side */
  .card-back { background: var(--card-blue); }
  .card-back .drone-visual {
    position: absolute; right: 40px; top: 30px;
    width: 400px; height: 360px; border-radius: 50%;
    background: radial-gradient(circle at 50% 45%, rgba(255,255,255,.28), rgba(92,182,240,.35) 45%, transparent 72%);
  }
  .divider {
    position: absolute; left: 0; right: 0; top: 150px; height: 7px;
    background: var(--white);
  }
  .identity {
    position: absolute; left: 270px; top: 126px;
    background: var(--card-blue);
    padding: 0 18px 4px;
    color: var(--white);
  }
  .identity .name { font-size: 40px; font-weight: 700; line-height: 1.1; }
  .identity .role { font-size: 15px; font-weight: 400; letter-spacing: .5px; }
  .contact {
    position: absolute; color: var(--white);
    display: flex; align-items: center; gap: 14px;
    font-size: 21px;
  }
  .contact svg { flex: none; }
  .contact-phone { left: 40px; top: 200px; }
  .contact-email { left: 250px; top: 270px; }
</style>
</head>
<body>
<main class="sheet">
  <section class="card card-front">
    <div class="scene-photo" role="img" aria-label="Blurred city skyline at dusk with glowing orange lights"></div>
    <div class="drone-photo" role="img" aria-label="White quadcopter drone with camera hovering in the air"></div>
    <div class="license-tag">ZQB# 90817263</div>
    <h1 class="headline">
      <span class="line-one">Aerial</span>
      <span class="line-two">Photography</span>
    </h1>
  </section>

  <section class="card card-back">
    <div class="drone-visual" role="img" aria-label="Faded photo of a white quadcopter drone seen from below"></div>
    <div class="divider"></div>
    <div class="identity">
      <p class="name">Name Here</p>
      <p class="role">PHOTOGRAPHER</p>
    </div>
    <div class="contact contact-phone">
      <svg width="26" height="40" viewBox="0 0 26 40" fill="none" stroke="#fff" stroke-width="2.5" stroke-linejoin="round">
        <path d="M8 2 L13 3 L13 12 L9 14 Q9 22 12 28 L16 27 L21 34 L16 38 Q4 34 3 18 Q3 6 8 2 Z"/>
      </svg>
      <span>(000) 123-4567</span>
    </div>
    <div class="contact contact-email">
      <svg width="50" height="36" viewBox="0 0 50 36" fill="none" stroke="#fff" stroke-width="3" stroke-linejoin="round">
        <rect x="2" y="2" width="46" height="32" rx="3"/>
        <path d="M2 4 L25 22 L48 4"/>
      </svg>
      <span>name@email.com</span>
    </div>
  </section>
</main>
</body>
</html>
```